Website for a Construction Business That Builds Houses

We want some design concepts for this website. Customer likes this competitor site: https://brenwickdwellings.com.au/

We have a logo for Tarvond Constructions. Logo font is Birdman, attached with AI.

Want to be able to change hero images

Will have a contact page.

Need to know what plugins will be used for WordPress.

Coding

Coded - Design and coding required

```html
<!DOCTYPE html>
<html lang="en">
<head>
<meta charset="utf-8">
<title>Tarvond Constructions</title>
<link rel="stylesheet" href="https://fonts.googleapis.com/css2?family=Poppins:wght@400;500;600&display=swap">
<style>
:root{
  --green:#7fc241;
  --green-text:#8ed33c;
  --ink:#111;
  --muted:#777;
  --white:#fff;
  --blog-bg:#f0fadf;
  --footer:#253e0a;
  --card-line:#cfcfcf;
}
*{margin:0;padding:0;box-sizing:border-box}
html,body{width:1200px;height:3759px;overflow:hidden}
body{position:relative;font-family:'Poppins',sans-serif;color:var(--ink);background:var(--white)}
.abs{position:absolute}
.btn{position:absolute;display:flex;align-items:center;justify-content:center;background:var(--green);color:var(--white);border-radius:24px;font-size:15px;width:160px;height:46px}
.center{left:0;width:1200px;text-align:center}

/* header */
.site-header{left:0;top:0;width:1200px;height:139px;background:var(--white)}
.brand{left:46px;top:30px;width:164px;height:182px;background:var(--white);z-index:3;display:flex;flex-direction:column;align-items:center;justify-content:center;gap:6px}
.brand-mark{width:40px;height:40px;background:var(--green)}
.brand-name{font-size:19px;font-weight:500;color:var(--ink);text-align:center;line-height:1.15}
.nav{top:68px;font-size:15px;color:var(--ink)}

/* hero */
.hero{left:0;top:139px;width:1200px;height:507px;background:linear-gradient(90deg,#7a4a2c 0%,#3f6a3a 25%,#2f5a2a 50%,#4d7a25 75%,#8aa63a 100%)}
.hero-shade{left:0;top:139px;width:1200px;height:507px;background:rgba(0,0,0,.25)}
.hero-kicker{top:266px;font-size:18px;color:var(--white)}
.hero-title{top:308px;font-size:48px;font-weight:600;color:var(--white);line-height:58px}

/* about */
.about-photo{left:182px;top:735px;width:352px;height:392px;border-radius:16px;background:linear-gradient(160deg,#e4e4e2,#b9b5ae 60%,#6d5c4a)}
.about-title{left:573px;top:758px;font-size:40px;font-weight:600}
.about-copy{left:573px;top:842px;width:448px;font-size:15.5px;line-height:19.2px}

/* projects */
.section-title{font-size:40px;font-weight:600}
.project{top:1323px;width:316px;height:316px}
.project-overlay{left:0;top:0;width:316px;height:316px;background:rgba(20,60,70,.55);padding:22px 6px}
.project-overlay h3{font-size:20px;font-weight:400;color:var(--green-text)}
.project-overlay p{margin-top:16px;font-size:15px;line-height:19px;color:var(--white)}
.read-more{position:absolute;left:6px;top:251px;width:126px;height:32px;font-size:15px;border-radius:16px;background:var(--green);color:var(--white);display:flex;align-items:center;justify-content:center}
.dot{position:absolute;width:16px;height:16px;border-radius:50%;background:var(--green)}
.dot.hollow{background:transparent;border:2px solid var(--green)}

/* cta */
.cta{left:0;top:1744px;width:1200px;height:401px;background:linear-gradient(90deg,#4a4a4a,#2e2e2e 50%,#1a1a1a)}
.cta-text{top:1820px;font-size:40px;font-weight:600;color:var(--white);line-height:48px}

/* blog */
.blog{left:0;top:2145px;width:1200px;height:705px;background:var(--blog-bg)}
.blog-card{top:2280px;width:359px;height:421px;background:var(--white);border:2px solid var(--card-line)}
.blog-img{position:absolute;left:20px;top:10px;width:317px;height:206px}
.blog-date{position:absolute;left:20px;top:248px;font-size:15px}
.blog-cat{position:absolute;left:20px;top:286px;font-size:15px;color:var(--muted)}
.blog-head{position:absolute;left:20px;top:328px;width:320px;font-size:20px;line-height:24px}

/* testimonials */
.testi-title{top:2870px;font-size:40px;font-weight:400}
.avatar{width:104px;height:104px;border-radius:50%;background:linear-gradient(160deg,#8a8a8a,#2b2b2b)}
.quote{font-size:15px;line-height:19px;width:240px}
.who{font-size:20px}

/* footer */
.footer{left:0;top:3147px;width:1200px;height:612px;background:var(--footer);color:var(--white)}
.foot-brand{left:44px;top:3233px;width:168px;height:180px;background:var(--white);display:flex;flex-direction:column;align-items:center;justify-content:center;gap:6px}
.foot-head{font-size:20px;font-weight:500;color:var(--white)}
.foot-text{font-size:15px;color:var(--white);line-height:19px}
.social{top:3344px;width:36px;height:36px;border:3px solid var(--white);border-radius:50%}
</style>
</head>
<body>

<header class="abs site-header"></header>
<div class="abs brand"><div class="brand-mark"></div><div class="brand-name">Tarvond<br>Constructions</div></div>
<span class="abs nav" style="left:723px">Home</span>
<span class="abs nav" style="left:797px">About Us</span>
<span class="abs nav" style="left:894px">Our Services</span>
<span class="abs nav" style="left:1018px">Blog</span>
<span class="abs nav" style="left:1078px">Contact Us</span>

<section>
  <div class="abs hero" role="img" aria-label="Photo of a timber-clad house with a green door beside leafy garden trees"></div>
  <div class="abs hero-shade"></div>
  <p class="abs center hero-kicker">KNOCK DOWN AND REBUILD</p>
  <h1 class="abs center hero-title">Happy with your location<br>but need a upgrade ?</h1>
  <a class="btn" style="left:520px;top:472px">Contact Us</a>
</section>

<section>
  <div class="abs about-photo" role="img" aria-label="Photo of a man relaxing in a lounge chair with his dog beside a potted plant"></div>
  <h2 class="abs about-title">About Us</h2>
  <p class="abs about-copy">Lorem ipsum dolor sit amet, consectetur adipiscing elit, sed do eiusmod tempor incididunt ut labore et dolore magna aliqua. Quis ipsum suspendisse ultrices gravida. Risus commodo viverra maecenas accumsan lacus vel facilisis. Lorem ipsum dolor sit amet, consectetur adipiscing elit, sed do eiusmod tempor incididunt ut labore et dolore magna aliqua. Quis ipsum suspendisse ultrices gravida. Risus commodo viverra maecenas accumsan lacus vel facilisis.</p>
  <a class="btn" style="left:573px;top:1049px">Contact Us</a>
</section>

<section>
  <h2 class="abs center section-title" style="top:1220px">Our Projects</h2>
  <div class="abs project" style="left:85px;background:linear-gradient(160deg,#3a8c8c,#2c6b70 50%,#a08a3a)" role="img" aria-label="Photo of a hospital ward room">
    <div class="abs project-overlay">
      <h3>Hospitals</h3>
      <p>Lorem ipsum dolor sit amet, consectetur adipiscing elit, sed do eiusmod tempor incididunt ut labore et dolore magna aliqua. Quis ipsum suspendisse ultrices gravida. Risus commodo viverra</p>
      <span class="read-more">Read More</span>
    </div>
  </div>
  <div class="abs project" style="left:442px;background:linear-gradient(170deg,#dcdcdc,#7a5a40 55%,#4a3a2a)" role="img" aria-label="Photo of a modern apartment building with timber balconies"></div>
  <div class="abs project" style="left:800px;background:linear-gradient(180deg,#5a4a8a,#c06a8a 45%,#f09a6a 60%,#3a2a4a)" role="img" aria-label="Illustration of an office meeting room overlooking a sunset city"></div>
  <span class="dot hollow" style="left:568px;top:1674px"></span>
  <span class="dot" style="left:591px;top:1674px"></span>
  <span class="dot" style="left:614px;top:1674px"></span>
</section>

<section>
  <div class="abs cta" role="img" aria-label="Dark photo of a modern two-storey home exterior"></div>
  <h2 class="abs center cta-text">Excited at the prospect of a Knock Down<br>Rebuild project?<br>Contact us today to discover what’s possible.</h2>
  <a class="btn" style="left:512px;top:2022px">Contact Us</a>
</section>

<section>
  <div class="abs blog"></div>
  <h2 class="abs center section-title" style="top:2180px">Blog</h2>
  <article class="abs blog-card" style="left:40px">
    <div class="blog-img" style="background:linear-gradient(160deg,#e8e8e8,#9a9a9a)" role="img" aria-label="Photo of two people toasting with wine glasses"></div>
    <span class="blog-date">July 2, 2020</span>
    <span class="blog-cat">Colour, New build</span>
    <h3 class="blog-head" style="font-weight:400">Choosing a colour palette for your new home</h3>
  </article>
  <article class="abs blog-card" style="left:421px">
    <div class="blog-img" style="background:linear-gradient(160deg,#2a2a2a,#8a6a4a 50%,#1a1a1a)" role="img" aria-label="Photo of a parent and child at a bunk bed"></div>
    <span class="blog-date" style="top:240px">July 2, 2020</span>
    <span class="blog-cat">First home builder, New build</span>
    <h3 class="blog-head" style="font-weight:400">Some useful terminology for first home builders!</h3>
  </article>
  <article class="abs blog-card" style="left:802px">
    <div class="blog-img" style="background:linear-gradient(160deg,#f0ece4,#c8b890 55%,#6a4a3a)" role="img" aria-label="Photo of a furnished living room with framed wall art"></div>
    <span class="blog-date" style="top:252px">July 2, 2020</span>
    <span class="blog-cat" style="top:290px">First home builder, grants, New build</span>
    <h3 class="blog-head" style="font-weight:400;top:330px">Information about the new HomeBuilder grant</h3>
  </article>
  <span class="dot hollow" style="left:568px;top:2751px"></span>
  <span class="dot" style="left:591px;top:2751px"></span>
  <span class="dot" style="left:614px;top:2751px"></span>
</section>

<section>
  <h2 class="abs center testi-title">Testimonials</h2>
  <svg class="abs" style="left:66px;top:3030px" width="20" height="24" viewBox="0 0 20 24"><path d="M14 2 L4 12 L14 22" fill="none" stroke="#111" stroke-width="3"/></svg>
  <svg class="abs" style="left:1118px;top:3030px" width="20" height="24" viewBox="0 0 20 24"><path d="M6 2 L16 12 L6 22" fill="none" stroke="#111" stroke-width="3"/></svg>
  <div class="abs avatar" style="left:201px;top:2990px" role="img" aria-label="Portrait photo of John"></div>
  <p class="abs quote" style="left:331px;top:2998px">Lorem ipsum dolor sit amet, consectetur adipiscing elit, sed do eiusmod tempor</p>
  <span class="abs who" style="left:329px;top:3070px">John</span>
  <div class="abs avatar" style="left:628px;top:2994px" role="img" aria-label="Portrait photo of Peter"></div>
  <p class="abs quote" style="left:757px;top:3002px">Lorem ipsum dolor sit amet, consectetur adipiscing elit, sed do eiusmod tempor</p>
  <span class="abs who" style="left:757px;top:3076px">Peter</span>
</section>

<footer>
  <div class="abs footer"></div>
  <div class="abs foot-brand"><div class="brand-mark"></div><div class="brand-name">Tarvond<br>Constructions</div></div>

  <h4 class="abs foot-head" style="left:430px;top:3290px">Address</h4>
  <svg class="abs" style="left:392px;top:3356px" width="22" height="32" viewBox="0 0 22 32"><path d="M11 1C5.5 1 1 5.5 1 11c0 8 10 20 10 20s10-12 10-20C21 5.5 16.5 1 11 1z" fill="#fff"/><circle cx="11" cy="11" r="4" fill="#253e0a"/></svg>
  <p class="abs foot-text" style="left:429px;top:3359px">14 Wattlebank Rd,<br>Coomera QLD 4209</p>
  <svg class="abs" style="left:392px;top:3437px" width="20" height="20" viewBox="0 0 24 24"><path d="M6.6 10.8a15 15 0 0 0 6.6 6.6l2.2-2.2c.3-.3.7-.4 1-.2 1.1.4 2.3.6 3.6.6.6 0 1 .4 1 1V20c0 .6-.4 1-1 1A17 17 0 0 1 3 4c0-.6.4-1 1-1h3.5c.6 0 1 .4 1 1 0 1.3.2 2.5.6 3.6.1.3 0 .7-.2 1z" fill="#fff"/></svg>
  <p class="abs foot-text" style="left:429px;top:3438px">1300 555 014</p>

  <h4 class="abs foot-head" style="left:681px;top:3286px">Quick Links</h4>
  <span class="abs foot-text" style="left:682px;top:3358px">Home</span>
  <span class="abs foot-text" style="left:682px;top:3397px">About Us</span>
  <span class="abs foot-text" style="left:682px;top:3435px">Our Services</span>
  <span class="abs foot-text" style="left:682px;top:3474px">Snaps</span>
  <span class="abs foot-text" style="left:682px;top:3512px">Job</span>
  <span class="abs foot-text" style="left:682px;top:3551px">Contact Us</span>

  <h4 class="abs foot-head" style="left:952px;top:3286px">Follow Us</h4>
  <span class="abs social" style="left:914px"></span>
  <span class="abs social" style="left:966px"></span>
  <span class="abs social" style="left:1016px"></span>
  <span class="abs social" style="left:1066px"></span>

  <p class="abs center foot-text" style="top:3683px">© Tarvond Constructions Pty Ltd 2023</p>
</footer>

</body>
</html>
```